Author book launch promotion design for social media

We are organising an authors book launch event and require an author promotion design that will be used on social media (Chatterbook, netted) promotion.

The design must have the author's photo, image of their book, the event logo, details of the event plus website address (penfairhall.com.au).

Details of the event can be found at penfairhall.com.au.

the design has to be attractive and inviting and colours in accordance with the brand colours.

You can choose 1 one of the book images attached
Author name: Dr Tarek Bismil
Event Details
LAUNCH YOUR BOOK IN STYLE

Quillmark Reading Fair and Showcase 2022
7 - 8 October 2022
Melbourne Larkvale Centre
14 Corrigal St, Southbank Melbourne

For registration and ticketing visit:
penfairhall.com.au

I have attached also a sample promo. Please be creative.

```html
<!DOCTYPE html>
<html lang="en">
<head>
<meta charset="utf-8">
<title>Launch Your Book in Style – Dr Tarek Bismil</title>
<link rel="stylesheet" href="https://fonts.googleapis.com/css2?family=Montserrat:wght@600;700;800&display=swap">
<style>
  :root {
    --rose: #d7495b;
    --gold: #f2a531;
    --teal: #188790;
    --teal-text: #1f7190;
    --navy: #23466a;
    --band: #3b6891;
    --white: #ffffff;
    --paper: #ffffff;
  }
  * { margin: 0; padding: 0; box-sizing: border-box; }
  html, body { width: 1200px; height: 1070px; overflow: hidden; background: var(--paper); }
  body { font-family: "Montserrat", Arial, sans-serif; }
  .promo { position: relative; width: 1200px; height: 1070px; overflow: hidden; background: var(--paper); }

  .backdrop-portrait {
    position: absolute; left: 420px; top: 150px; width: 780px; height: 780px;
    background: radial-gradient(ellipse at 50% 45%, #dcdde0 0%, #e8e9eb 45%, rgba(255,255,255,0) 75%);
    opacity: .8;
  }
  .corner-shapes { position: absolute; left: 0; top: 0; width: 1200px; height: 460px; }

  .headline {
    position: absolute; left: 76px; top: 52px; color: var(--white);
    font-weight: 800; text-transform: uppercase; line-height: 1;
  }
  .headline .line-one { display: block; font-size: 66px; letter-spacing: .5px; }
  .headline .line-two { display: block; font-size: 82px; margin-top: 6px; }

  .event-mark {
    position: absolute; left: 950px; top: 112px; width: 220px;
    display: flex; align-items: center; gap: 12px;
  }
  .event-mark .mark-square { width: 24px; height: 24px; background: var(--gold); flex: none; }
  .event-mark .mark-name { color: var(--gold); font-weight: 800; font-size: 28px; line-height: 1.05; }

  .ticket-band {
    position: absolute; left: 0; top: 946px; width: 1200px; height: 124px;
    background: var(--band);
  }

  .author-photo {
    position: absolute; left: 0; top: 245px; width: 560px; height: 825px;
    background: linear-gradient(180deg, #3a3b40 0%, #2a2b30 60%, #1f2024 100%);
    clip-path: polygon(170px 0, 390px 0, 425px 130px, 455px 200px, 462px 560px, 525px 700px, 530px 825px, 0 825px, 0 250px, 110px 180px);
  }

  .book-image {
    position: absolute; left: 812px; top: 280px; width: 318px; height: 440px;
    background: linear-gradient(160deg, #f4f4f4 0%, #d9d9db 55%, #a9abb0 100%);
    box-shadow: 0 10px 24px rgba(0,0,0,.18);
  }

  .author-banner {
    position: absolute; left: 377px; top: 382px; width: 490px; height: 94px;
    background: var(--teal); display: flex; align-items: center; padding-left: 34px;
    color: var(--white); font-weight: 800; font-size: 42px;
  }

  .event-name {
    position: absolute; right: 338px; top: 500px; text-align: right;
    color: var(--teal-text); font-weight: 700; font-size: 31px; line-height: 1.35;
  }

  .event-details { position: absolute; right: 72px; top: 728px; text-align: right; }
  .event-date { color: var(--rose); font-weight: 800; font-size: 45px; line-height: 1.1; margin-bottom: 14px; }
  .venue { color: var(--navy); font-weight: 700; font-size: 31px; line-height: 1.42; }

  .ticket-text {
    position: absolute; right: 72px; top: 960px; text-align: right;
    font-weight: 700; font-size: 31px; line-height: 1.5;
  }
  .ticket-text .invite { color: var(--white); }
  .ticket-text .site { color: var(--gold); }
</style>
</head>
<body>
  <main class="promo">
    <div class="backdrop-portrait" role="img" aria-label="Faint enlarged portrait of the author as background decoration"></div>

    <svg class="corner-shapes" viewBox="0 0 1200 460" aria-hidden="true">
      <polygon points="0,0 1150,0 0,378" fill="var(--rose)"/>
      <polygon points="0,378 1150,0 1200,0 1200,6 0,422" fill="var(--gold)"/>
    </svg>

    <h1 class="headline">
      <span class="line-one">Launch your book</span>
      <span class="line-two">In style</span>
    </h1>

    <div class="event-mark">
      <span class="mark-square"></span>
      <span class="mark-name">QUILLMARK FAIR</span>
    </div>

    <div class="ticket-band"></div>

    <div class="author-photo" role="img" aria-label="Photo of author Dr Tarek Bismil in a dark suit giving a thumbs up"></div>

    <div class="book-image" role="img" aria-label="Cover of the author's book standing on a second copy"></div>

    <div class="author-banner">Dr Tarek Bismil</div>

    <p class="event-name">Quillmark Reading Fair<br>and Showcase 2022</p>

    <div class="event-details">
      <p class="event-date">7 - 8 October 2022</p>
      <p class="venue">Melbourne Larkvale Centre<br>14 Corrigal St<br>Southbank Melbourne</p>
    </div>

    <p class="ticket-text">
      <span class="invite">For registration and ticketing visit</span><br>
      <span class="site">penfairhall.com.au</span>
    </p>
  </main>
</body>
</html>
```